Fintech company needs ads created around "can't afford help"

Design 3 ads (total) that focus around HELPING people who can't afford to get help with their finances.

The 3 ads will be made up of 1 design for each audience:
• Millennial
• Generation X
• Baby Boomer

We are testing campaigns in Chatterloop that will drive to a landing page. We are an online financial-tech company who helps people manage their retirement account. We’re looking for creative talent who are effective at developing imagery to be used in Chatterloop to grab people’s attention and drive clicks. Because of the scrutiny in our industry, we’ll handle the ad copy above and below the imagery you create. We encourage you to use/not use words in your creative.

Target Market(s)

• Millennial
• Generation X
• Baby Boomer

Industry/Entity Type

Financial Service

Requirements
Must have
• Image Dimensions
• Width: 1200 Height: 628
• Final PSD Designs
• Feel free to play around with any color scheme.
• Tasteful – we are not a traditional, stodgy Wall Street Financial firm, but we need to convey that we are trustworthy and legitimate.
Nice to have
• You are not limited to photos – whatever you believe will stand out and engage with prospective clients is fair game (including illustrations, animation, video, etc).
• Think about how your work could translate into other forms such as motion graphics or video.
• Ultimately, we will test our favorites and come back to those with the highest performance which will turn into additional work and additional formats.
Should not have
• • No stock photography UNLESS found at Pixvarra (we will pay for the image)
• • No Testimonials – regulations prevent us from using testimonials in our advertisements

```html
<!DOCTYPE html>
<html lang="en">
<head>
<meta charset="utf-8">
<title>Helping people with their finances – ad</title>
<link rel="stylesheet" href="https://fonts.googleapis.com/css2?family=Montserrat:wght@300;400;700&display=swap">
<style>
  :root {
    --stage: #1a1a1a;
    --panel-dark: #1f2023;
    --accent-blue: #1fb6ee;
    --text-light: #f2f4f6;
    --photo-light: #dfe3e8;
    --photo-mid: #9aa4b0;
    --photo-suit: #5d6673;
    --stripe: rgba(255, 255, 255, 0.75);
  }
  * { margin: 0; padding: 0; box-sizing: border-box; }
  html, body {
    width: 1200px;
    height: 808px;
    overflow: hidden;
    background: var(--stage);
  }
  .ad {
    position: absolute;
    left: 0;
    top: 90px;
    width: 1200px;
    height: 628px;
    overflow: hidden;
    background: var(--panel-dark);
  }
  .ad-art {
    position: absolute;
    inset: 0;
    width: 1200px;
    height: 628px;
  }
  .logo-box {
    position: absolute;
    left: 69px;
    top: 69px;
    width: 204px;
    height: 120px;
    border: 2px solid var(--text-light);
    display: flex;
    align-items: center;
    justify-content: center;
    font-family: "Montserrat", sans-serif;
    font-weight: 400;
    font-size: 37px;
    letter-spacing: 1px;
    color: var(--text-light);
  }
  .headline {
    position: absolute;
    left: 60px;
    top: 408px;
    font-family: "Montserrat", sans-serif;
    font-weight: 300;
    font-size: 43px;
    line-height: 55px;
    color: var(--text-light);
    white-space: nowrap;
  }
  .headline .lead {
    color: var(--accent-blue);
    font-weight: 400;
  }
  .headline .emphasis {
    color: var(--accent-blue);
    font-weight: 700;
  }
</style>
</head>
<body>
  <div class="ad">
    <svg class="ad-art" viewBox="0 0 1200 628" xmlns="http://www.w3.org/2000/svg">
      <defs>
        <linearGradient id="officePhoto" x1="0" y1="0" x2="1" y2="1">
          <stop offset="0" stop-color="#6b6f76"/>
          <stop offset="0.45" stop-color="#b8bec6"/>
          <stop offset="0.75" stop-color="#8f98a4"/>
          <stop offset="1" stop-color="#4e5561"/>
        </linearGradient>
        <linearGradient id="darkVeil" x1="0" y1="0" x2="0" y2="1">
          <stop offset="0" stop-color="#232428" stop-opacity="0.92"/>
          <stop offset="1" stop-color="#1b1c1f" stop-opacity="0.96"/>
        </linearGradient>
      </defs>
      <rect class="photo-office" role="img" aria-label="Photo of a smiling young businessman in a grey suit at an office meeting, colleagues blurred behind him" x="0" y="0" width="1200" height="628" fill="url(#officePhoto)"/>
      <polygon class="band-soft" points="560,0 1200,0 1200,628 760,628" fill="#ffffff" fill-opacity="0.08"/>
      <polygon class="veil-dark" points="0,0 399,0 702,628 0,628" fill="url(#darkVeil)"/>
      <polygon class="stripe-light" points="399,0 432,0 735,628 702,628" fill="var(--stripe)"/>
      <polygon class="stripe-mid" points="432,0 560,0 840,628 735,628" fill="#2a2c31" fill-opacity="0.35"/>
      <polygon class="stripe-edge" points="1124,0 1150,0 1200,104 1200,158" fill="#ffffff" fill-opacity="0.35"/>
    </svg>

    <div class="logo-box">LOGO</div>

    <p class="headline">
      <span class="lead">HELPING</span> people who<br>
      can't afford to get help<br>
      with <span class="emphasis">their finances</span>
    </p>
  </div>
</body>
</html>
```